Marketing based tech company needs infographics

I need an infographic created about our process as it pertains to event organizers working with marketers, marketers working with event organizers and both working with sponsors.

3 sections
Event Organizers Steps: Total Timeline 3-10 days
1. Event organizer submits their deck (proposal)
2. It is sent to a vetter for review
3. The vetter provides edits
4. The event organizer approves the edits
5. The deck is turned into a website link
6. The deck is ready for the event organizer to send to sponsors
7. Sponsors open it and are wowed!
Marketer Steps: Total timeline 3-10 days
1. the marketer receives the deck
2. Provides feedback/edits to the event organizer
3. The event organizer approves the edits
6. The vetter is paid for their work immediately after the website goes live
Sponsors Steps: Total Timeline 30+ days
1. Sponsor is matched only with events that meet their demographics.
2. Event organizer submits their deck (proposal) to sponsor
3. The sponsor reviews the deck
4. If they are wowed they continue the conversation.
5. The event terms are negotiated.
6. The event organizer is paid 14 days prior to the event.
7. The event happens and is a success!

Target Market(s)

Minority-owned businesses and event planners.

Industry/Entity Type

Marketing

Font styles to use
Sans Serif

Colors
f78f20
0455a3
0692cd

Requirements
Must have
• 3 sections
• Event Organizers Steps: Total Timeline 3-10 days
• 1. Event organizer submits their deck (proposal)
• 2. It is sent to a vetter for review
• 3. The vetter provides edits
• 4. The event organizer approves the edits
• 5. The deck is turned into a website link
• 6. The deck is ready for the event organizer to send to sponsors
• 7. Sponsors open it and are wowed!
• Marketer Steps: Total timeline 3-10 days
• 1. the marketer receives the deck
• 2. Provides feedback/edits to the event organizer
• 3. The event organizer approves the edits
• 6. The vetter is paid for their work immediately after the website goes live
• Sponsors Steps: Total Timeline 30+ days
• 1. Sponsor is matched only with events that meet their demographics.
• 2. Event organizer submits their deck (proposal) to sponsor
• 3. The sponsor reviews the deck
• 4. If they are wowed they continue the conversation.
• 5. The event terms are negotiated.
• 6. The event organizer is paid 14 days prior to the event.
• 7. The event happens and is a success!
Nice to have
• To incorporate the styles of the graphics and icons attached
Should not have
• Be creative!

```html
<!DOCTYPE html>
<html lang="en">
<head>
<meta charset="utf-8">
<title>Process Infographic</title>
<link rel="stylesheet" href="https://fonts.googleapis.com/css2?family=Oswald:wght@500;700&family=Open+Sans:wght@400;600;700&display=swap">
<style>
:root{
  --orange:#f78f20;
  --navy:#0455a3;
  --sky:#0692cd;
  --white:#ffffff;
  --ink:#1d2a3a;
}
*{box-sizing:border-box;margin:0;padding:0}
html,body{width:1200px;height:2552px;overflow:hidden;background:var(--white)}
body{position:relative;font-family:"Open Sans",Arial,sans-serif;color:var(--ink)}
.section{position:absolute;left:0;width:1200px}
.organizers{top:0;height:850px;background:var(--white)}
.marketers{top:850px;height:740px;background:var(--navy)}
.sponsors{top:1590px;height:840px;background:var(--orange)}
.footer{top:2430px;height:122px;background:var(--white)}

.title{position:absolute;left:0;width:1200px;text-align:center;font-family:"Oswald",Arial,sans-serif;font-weight:700;text-transform:uppercase;line-height:1}
.organizers .title{top:30px;font-size:108px;color:var(--navy);letter-spacing:1px}
.marketers .title,.sponsors .title{top:48px;font-size:116px;color:var(--white);letter-spacing:22px}

.rule{position:absolute;left:90px;width:1020px;height:14px;display:flex}
.rule span{flex:1}
.organizers .rule{top:150px}
.organizers .rule .a{background:var(--orange)} .organizers .rule .b{background:var(--navy)}
.marketers .rule,.sponsors .rule{top:185px}
.marketers .rule .a{background:var(--orange)} .marketers .rule .b{background:var(--sky)}
.sponsors .rule .a{background:var(--navy)} .sponsors .rule .b{background:var(--white)}

.timeline{position:absolute;right:90px;display:flex;align-items:center;gap:12px;font-family:"Oswald",Arial,sans-serif;font-weight:500;font-size:40px;text-transform:uppercase;letter-spacing:1px}
.timeline svg{width:44px;height:44px}
.organizers .timeline{top:174px;color:var(--navy)}
.marketers .timeline,.sponsors .timeline{top:208px;color:var(--white)}

.step{position:absolute;width:250px}
.step .ring{width:168px;height:168px;border-radius:50%;background:var(--white);display:flex;align-items:center;justify-content:center;margin:0 auto}
.organizers .ring{border:8px solid var(--navy);color:var(--navy)}
.sponsors .ring{width:140px;height:140px;color:var(--navy)}
.ring svg{width:84px;height:84px}
.sponsors .ring svg{width:70px;height:70px}
.caption{display:flex;gap:10px;margin-top:22px;font-size:21px;line-height:1.3;font-weight:600}
.organizers .caption{color:var(--ink)}
.sponsors .caption{color:var(--white);flex-direction:column;align-items:center;text-align:center;font-size:18px;gap:6px;margin-top:12px}
.num{flex:none;width:38px;height:38px;border-radius:50%;display:flex;align-items:center;justify-content:center;font-weight:700;font-size:21px;color:var(--white)}
.organizers .num{background:var(--orange)}
.sponsors .num{background:var(--navy);width:34px;height:34px;font-size:18px}

.arrow{position:absolute;width:26px;height:34px}
.organizers .arrow{fill:var(--sky)}
.sponsors .arrow{fill:var(--white)}

.card{position:absolute;height:88px;border:3px solid var(--white);display:flex;align-items:center;gap:14px;padding:0 16px;color:var(--white);font-size:21px;font-weight:600;line-height:1.25}
.card svg{flex:none;width:50px;height:50px;color:var(--white)}
.card .num{background:var(--white);color:var(--navy);width:36px;height:36px;font-size:19px}
.col-left{left:110px;width:470px}
.col-right{left:620px;width:470px}

.brand{position:absolute;left:0;width:1200px;top:20px;height:82px;display:flex;justify-content:center;align-items:center;gap:18px}
.brand .dot{width:52px;height:52px;border-radius:50%;background:var(--orange)}
.brand .name{font-family:"Open Sans",Arial,sans-serif;font-weight:700;font-size:64px;line-height:1;color:var(--navy);letter-spacing:1px}
</style>
</head>
<body>

<svg width="0" height="0" style="position:absolute" aria-hidden="true">
  <defs>
    <symbol id="i-cal" viewBox="0 0 48 48"><rect x="5" y="9" width="38" height="34" rx="3" fill="none" stroke="currentColor" stroke-width="4"/><rect x="5" y="9" width="38" height="9" fill="currentColor"/><line x1="14" y1="4" x2="14" y2="13" stroke="currentColor" stroke-width="4"/><line x1="34" y1="4" x2="34" y2="13" stroke="currentColor" stroke-width="4"/><g fill="currentColor"><rect x="11" y="23" width="6" height="5"/><rect x="21" y="23" width="6" height="5"/><rect x="31" y="23" width="6" height="5"/><rect x="11" y="32" width="6" height="5"/><rect x="21" y="32" width="6" height="5"/></g></symbol>
    <symbol id="i-upload" viewBox="0 0 48 48"><path d="M6 30v12h36V30" fill="none" stroke="currentColor" stroke-width="4"/><path d="M24 32V8M14 18l10-10 10 10" fill="none" stroke="currentColor" stroke-width="4"/></symbol>
    <symbol id="i-send" viewBox="0 0 48 48"><path d="M44 4 4 22l16 6 6 16z" fill="none" stroke="currentColor" stroke-width="3.5" stroke-linejoin="round"/><path d="M44 4 20 28" stroke="currentColor" stroke-width="3.5"/></symbol>
    <symbol id="i-edit" viewBox="0 0 48 48"><path d="M24 8H8v32h32V24" fill="none" stroke="currentColor" stroke-width="4"/><path d="M38 6l4 4-18 18-6 2 2-6z" fill="none" stroke="currentColor" stroke-width="3.5" stroke-linejoin="round"/></symbol>
    <symbol id="i-check" viewBox="0 0 48 48"><rect x="6" y="8" width="34" height="34" fill="none" stroke="currentColor" stroke-width="4"/><path d="M13 24l9 9 22-24" fill="none" stroke="currentColor" stroke-width="5"/></symbol>
    <symbol id="i-globe" viewBox="0 0 48 48"><circle cx="24" cy="24" r="18" fill="none" stroke="currentColor" stroke-width="3.5"/><ellipse cx="24" cy="24" rx="8" ry="18" fill="none" stroke="currentColor" stroke-width="3"/><path d="M6 24h36M9 15h30M9 33h30" stroke="currentColor" stroke-width="3"/></symbol>
    <symbol id="i-star" viewBox="0 0 48 48"><path d="M24 3l6 14 15 1-11 10 4 15-14-8-14 8 4-15L3 18l15-1z" fill="currentColor"/></symbol>
    <symbol id="i-hands" viewBox="0 0 48 48"><path d="M2 18l10-6 10 4 6-4 8 2 10 6-8 14-8 6-10-4-10-8z" fill="none" stroke="currentColor" stroke-width="3.5" stroke-linejoin="round"/><path d="M22 16l-6 8 4 2 8-6M18 32l4 4M24 30l4 4M30 28l3 3" fill="none" stroke="currentColor" stroke-width="3"/></symbol>
    <symbol id="i-chat" viewBox="0 0 48 48"><path d="M6 8h36v24H20l-10 8v-8H6z" fill="none" stroke="currentColor" stroke-width="4" stroke-linejoin="round"/><path d="M15 20l6 6 12-12" fill="none" stroke="currentColor" stroke-width="4"/></symbol>
    <symbol id="i-thumb" viewBox="0 0 48 48"><path d="M6 22h8v20H6zM16 22l8-14c4 0 5 3 4 7l-2 7h14c3 0 4 3 3 5l-4 12c-1 2-2 3-4 3H16z" fill="currentColor"/></symbol>
    <symbol id="i-www" viewBox="0 0 48 48"><circle cx="24" cy="24" r="19" fill="none" stroke="currentColor" stroke-width="3.5"/><text x="24" y="29" text-anchor="middle" font-family="Open Sans, Arial, sans-serif" font-weight="700" font-size="13" fill="currentColor">www</text></symbol>
    <symbol id="i-cash" viewBox="0 0 48 48"><rect x="3" y="12" width="42" height="24" rx="2" fill="none" stroke="currentColor" stroke-width="3.5"/><circle cx="24" cy="24" r="6" fill="none" stroke="currentColor" stroke-width="3"/><circle cx="10" cy="24" r="2" fill="currentColor"/><circle cx="38" cy="24" r="2" fill="currentColor"/></symbol>
    <symbol id="i-deck" viewBox="0 0 48 48"><rect x="6" y="6" width="36" height="26" fill="none" stroke="currentColor" stroke-width="3.5"/><path d="M24 32v10M16 42h16M12 26l8-8 6 5 10-10" fill="none" stroke="currentColor" stroke-width="3"/></symbol>
    <symbol id="i-bulb" viewBox="0 0 48 48"><path d="M24 10a11 11 0 0 0-7 19c2 2 3 4 3 6h8c0-2 1-4 3-6a11 11 0 0 0-7-19z" fill="none" stroke="currentColor" stroke-width="3.5"/><path d="M19 40h10M24 2v4M8 8l3 3M40 8l-3 3M3 22h4M41 22h4" stroke="currentColor" stroke-width="3"/></symbol>
    <symbol id="i-puzzle" viewBox="0 0 48 48"><path d="M8 14h10a5 5 0 1 1 10 0h10v10a5 5 0 1 0 0 10v8H8V32a5 5 0 1 0 0-10z" fill="currentColor"/></symbol>
    <symbol id="i-cycle" viewBox="0 0 48 48"><path d="M38 18A15 15 0 0 0 10 20M10 30a15 15 0 0 0 28-2" fill="none" stroke="currentColor" stroke-width="4"/><path d="M40 8v12H28M8 40V28h12" fill="none" stroke="currentColor" stroke-width="4"/></symbol>
    <symbol id="i-eye" viewBox="0 0 48 48"><path d="M3 24s8-13 21-13 21 13 21 13-8 13-21 13S3 24 3 24z" fill="none" stroke="currentColor" stroke-width="3.5"/><circle cx="24" cy="24" r="7" fill="currentColor"/></symbol>
    <symbol id="i-forward" viewBox="0 0 48 48"><path d="M4 32c4-10 14-14 24-14V8l16 14-16 14V26c-10 0-18 2-24 6z" fill="none" stroke="currentColor" stroke-width="3.5" stroke-linejoin="round"/></symbol>
    <symbol id="i-people" viewBox="0 0 48 48"><circle cx="16" cy="16" r="6" fill="currentColor"/><circle cx="32" cy="16" r="6" fill="currentColor"/><path d="M4 38c0-8 5-13 12-13s12 5 12 13zM26 26c2-1 4-1 6-1 7 0 12 5 12 13H30" fill="currentColor"/></symbol>
    <symbol id="i-paid" viewBox="0 0 48 48"><rect x="3" y="12" width="42" height="24" rx="3" fill="none" stroke="currentColor" stroke-width="3.5"/><text x="24" y="29" text-anchor="middle" font-family="Oswald, Arial, sans-serif" font-weight="700" font-size="14" fill="currentColor">PAID</text></symbol>
    <symbol id="i-burst" viewBox="0 0 48 48"><path d="M24 4v10M24 34v10M4 24h10M34 24h10M10 10l7 7M31 31l7 7M38 10l-7 7M17 31l-7 7" stroke="currentColor" stroke-width="4" stroke-linecap="round"/><circle cx="24" cy="24" r="4" fill="currentColor"/></symbol>
    <symbol id="i-tri" viewBox="0 0 26 34"><path d="M0 0l26 17L0 34z"/></symbol>
  </defs>
</svg>

<section class="section organizers">
  <h1 class="title">Event Organizers Steps</h1>
  <div class="rule"><span class="a"></span><span class="b"></span></div>
  <div class="timeline"><svg><use href="#i-cal"/></svg>Total Timeline 3-10 Days</div>

  <div class="step" style="left:135px;top:250px"><div class="ring"><svg><use href="#i-upload"/></svg></div><p class="caption"><span class="num">1</span><span>Event organizer submits their deck (proposal)</span></p></div>
  <svg class="arrow" style="left:423px;top:317px"><use href="#i-tri"/></svg>
  <div class="step" style="left:475px;top:250px"><div class="ring"><svg><use href="#i-send"/></svg></div><p class="caption"><span class="num">2</span><span>It is sent to a vetter for review</span></p></div>
  <svg class="arrow" style="left:763px;top:317px"><use href="#i-tri"/></svg>
  <div class="step" style="left:815px;top:250px"><div class="ring"><svg><use href="#i-edit"/></svg></div><p class="caption"><span class="num">3</span><span>The vetter provides edits</span></p></div>

  <div class="step" style="left:35px;top:530px"><div class="ring"><svg><use href="#i-check"/></svg></div><p class="caption"><span class="num">4</span><span>The event organizer approves the edits</span></p></div>
  <svg class="arrow" style="left:275px;top:597px"><use href="#i-tri"/></svg>
  <div class="step" style="left:320px;top:530px"><div class="ring"><svg><use href="#i-globe"/></svg></div><p class="caption"><span class="num">5</span><span>The deck is turned into a website link</span></p></div>
  <svg class="arrow" style="left:562px;top:597px"><use href="#i-tri"/></svg>
  <div class="step" style="left:608px;top:530px"><div class="ring"><svg><use href="#i-star"/></svg></div><p class="caption"><span class="num">6</span><span>The deck is ready for the event organizer to send to sponsors</span></p></div>
  <svg class="arrow" style="left:850px;top:597px"><use href="#i-tri"/></svg>
  <div class="step" style="left:900px;top:530px"><div class="ring"><svg><use href="#i-hands"/></svg></div><p class="caption"><span class="num">7</span><span>Sponsors open it and are wowed!</span></p></div>
</section>

<section class="section marketers">
  <h2 class="title">Marketer Steps</h2>
  <div class="rule"><span class="a"></span><span class="b"></span></div>
  <div class="timeline"><svg><use href="#i-cal"/></svg>Total Timeline 3-10 Days</div>

  <div class="card col-left" style="top:270px"><svg><use href="#i-upload"/></svg><span class="num">1</span><span>The marketer receives the deck</span></div>
  <div class="card col-right" style="top:270px"><svg><use href="#i-chat"/></svg><span class="num">2</span><span>Provides feedback/edits to the event organizer</span></div>
  <div class="card col-left" style="top:385px"><svg><use href="#i-thumb"/></svg><span class="num">3</span><span>The event organizer approves the edits</span></div>
  <div class="card col-right" style="top:385px"><svg><use href="#i-www"/></svg><span class="num">4</span><span>The deck is turned into a website link</span></div>
  <div class="card col-left" style="top:500px"><svg><use href="#i-cash"/></svg><span class="num">5</span><span>The vetter is paid for their work immediately after the website goes live</span></div>
  <div class="card col-right" style="top:500px"><svg><use href="#i-deck"/></svg><span class="num">6</span><span>The deck is ready for the event organizer to send to sponsors</span></div>
  <div class="card" style="top:612px;left:400px;width:400px;height:80px"><svg><use href="#i-bulb"/></svg><span class="num">7</span><span>Sponsors open it and are wowed!</span></div>
</section>

<section class="section sponsors">
  <h2 class="title">Sponsors Steps</h2>
  <div class="rule"><span class="a"></span><span class="b"></span></div>
  <div class="timeline"><svg><use href="#i-cal"/></svg>Total Timeline 3-10 Days</div>

  <div class="step" style="left:20px;top:275px"><div class="ring"><svg><use href="#i-puzzle"/></svg></div><p class="caption"><span class="num">1</span><span>Sponsor is matched only with events that meet their demographics</span></p></div>
  <svg class="arrow" style="left:270px;top:328px"><use href="#i-tri"/></svg>
  <div class="step" style="left:315px;top:275px"><div class="ring"><svg><use href="#i-cycle"/></svg></div><p class="caption"><span class="num">2</span><span>Event organizer submits their deck (proposal) to sponsor</span></p></div>
  <svg class="arrow" style="left:565px;top:328px"><use href="#i-tri"/></svg>
  <div class="step" style="left:610px;top:275px"><div class="ring"><svg><use href="#i-eye"/></svg></div><p class="caption"><span class="num">3</span><span>The sponsor reviews the deck</span></p></div>
  <svg class="arrow" style="left:860px;top:328px"><use href="#i-tri"/></svg>
  <div class="step" style="left:905px;top:275px"><div class="ring"><svg><use href="#i-forward"/></svg></div><p class="caption"><span class="num">4</span><span>If they are wowed they continue the conversation</span></p></div>

  <div class="step" style="left:105px;top:560px"><div class="ring"><svg><use href="#i-people"/></svg></div><p class="caption"><span class="num">5</span><span>The event terms are negotiated</span></p></div>
  <svg class="arrow" style="left:418px;top:613px"><use href="#i-tri"/></svg>
  <div class="step" style="left:475px;top:560px"><div class="ring"><svg><use href="#i-paid"/></svg></div><p class="caption"><span class="num">6</span><span>The event organizer is paid 14 days prior to the event</span></p></div>
  <svg class="arrow" style="left:788px;top:613px"><use href="#i-tri"/></svg>
  <div class="step" style="left:845px;top:560px"><div class="ring"><svg><use href="#i-burst"/></svg></div><p class="caption"><span class="num">7</span><span>The event happens and is a success!</span></p></div>
</section>

<footer class="section footer">
  <div class="brand"><span class="dot"></span><span class="name">PitchProof</span></div>
</footer>

</body>
</html>
```